RM Tomás Ferrier (Business Card)

Hi designers, in this work, I'm looking for an sophisticated stylish, elegant and proffesional personal card. We have a laboratory of pathology automated, with equipments high quality.
In this web the designers, have created my business logo, the name is "RM Tomás Ferrier"
In our lab, we principal work is to prepare the biopsies for further diagnostic of diseases like cancer, tumors, etc.
I need that the first face, only having my complete logo (Rm Tomás Ferrier, Laboratorio de procesamiento Histologico)
The overleaf, could repeat the same logo, like water logo.
In this face, I need to say: My full data:

Técnico en Anatomía Patológica
Tomás Ferrier Bustos M.P 48207
Av. Ramón Quiroga 817 - 2do piso - Instituto Brandeck.
Córdoba, Argentina
(0351) 156284930
ferrier.tomas@correoluz.com

with respect the colors of card, use your imagination, the original logo color is violet, I haven't chosen a color base for the card.

attached pictures are examples of cards I like your DESIGN.
Attached too, the original logo to my company.

the size of card are:
horizontal: 9cm
vertical: 5,5cm

any question that you have, not doubt to question me,
Hand to work!

Industry/Entity Type

Laboratory

Requirements
Must have
• designers sophisticated, not simples, like show the images attached

```html
<!DOCTYPE html>
<html lang="es">
<head>
<meta charset="utf-8">
<title>Tomás Ferrier – Tarjeta personal</title>
<link rel="stylesheet" href="https://fonts.googleapis.com/css2?family=Open+Sans:wght@400;600;700&display=swap">
<style>
  :root {
    --bg: #2a2a2c;
    --violet: #5e2a86;
    --violet-deep: #4a1f6c;
    --violet-mark: #532677;
    --grey: #8c8c8e;
    --grey-dark: #5a5a5c;
    --white: #ffffff;
    --lavender: #e4d8ef;
  }
  * { box-sizing: border-box; margin: 0; padding: 0; }
  html, body { width: 1200px; height: 900px; overflow: hidden; }
  body {
    background: var(--bg);
    font-family: "Open Sans", Arial, sans-serif;
    position: relative;
  }
  .card {
    position: absolute;
    left: 280px;
    width: 640px;
    height: 390px;
    border-radius: 24px;
    overflow: hidden;
  }
  .card-back {
    top: 45px;
    background: linear-gradient(135deg, #66318f 0%, var(--violet) 50%, var(--violet-deep) 100%);
  }
  .watermark {
    position: absolute;
    left: 0; right: 0; top: 165px;
    display: flex; align-items: center; justify-content: center; gap: 16px;
    white-space: nowrap;
  }
  .watermark-dot {
    width: 22px; height: 22px; border-radius: 50%;
    background: var(--violet-mark);
  }
  .watermark-name {
    font-weight: 700; font-size: 40px; color: var(--violet-mark);
    letter-spacing: 1px;
  }

  .card-front { top: 465px; background: var(--white); }
  .card-front svg.swoosh { position: absolute; inset: 0; }
  .brand {
    position: absolute; left: 0; right: 0; top: 34px;
    text-align: center;
  }
  .brand-mark {
    display: inline-flex; align-items: center; gap: 10px;
  }
  .brand-dot {
    width: 14px; height: 14px; border-radius: 50%; background: var(--violet);
  }
  .brand-name {
    font-weight: 600; font-size: 21px; letter-spacing: 7px; color: var(--grey-dark);
  }
  .brand-rule {
    width: 390px; height: 1px; background: var(--grey-dark);
    margin: 7px auto 5px;
  }
  .brand-tagline {
    font-weight: 600; font-size: 19px; color: var(--grey-dark);
    letter-spacing: -0.2px; white-space: nowrap;
  }
  .holder {
    position: absolute; left: 34px; top: 292px; color: var(--white);
  }
  .holder-name { font-weight: 700; font-size: 22px; letter-spacing: 0.3px; }
  .holder-role { font-weight: 400; font-size: 15px; color: var(--lavender); margin-top: 2px; }
  .holder-reg { font-weight: 600; font-size: 13px; letter-spacing: 1.5px; color: var(--lavender); margin-top: 14px; }
  .contact {
    position: absolute; right: 30px; top: 178px;
    text-align: right; color: var(--lavender);
    font-size: 14.5px; line-height: 20px;
    list-style: none;
  }
</style>
</head>
<body>
  <section class="card card-back" aria-label="Reverso de la tarjeta">
    <div class="watermark">
      <span class="watermark-dot"></span>
      <span class="watermark-name">RM Tomás Ferrier</span>
    </div>
  </section>

  <section class="card card-front" aria-label="Frente de la tarjeta">
    <svg class="swoosh" viewBox="0 0 640 390" width="640" height="390" aria-hidden="true">
      <defs>
        <linearGradient id="violetBody" x1="0" y1="0" x2="1" y2="1">
          <stop offset="0" stop-color="#66318f"/>
          <stop offset="1" stop-color="#4a1f6c"/>
        </linearGradient>
      </defs>
      <path d="M0,226 C180,216 380,194 560,156 C380,204 180,232 0,238 Z" fill="var(--violet)"/>
      <path d="M0,244 C200,222 420,170 640,118 L640,134 C420,186 200,240 0,266 Z" fill="var(--grey)"/>
      <path d="M0,266 C200,240 420,186 640,134 L640,390 L0,390 Z" fill="url(#violetBody)"/>
    </svg>

    <header class="brand">
      <div class="brand-mark">
        <span class="brand-dot"></span>
        <span class="brand-name">TOMÁS FERRIER</span>
      </div>
      <div class="brand-rule"></div>
      <div class="brand-tagline">LABORATORIO DE PROCESAMIENTO HISTOLOGICO</div>
    </header>

    <div class="holder">
      <div class="holder-name">TOMÁS FERRIER BUSTOS</div>
      <div class="holder-role">Técnico en Anatomía Patológica</div>
      <div class="holder-reg">M.P 48207</div>
    </div>

    <ul class="contact">
      <li>(0351) 156284930</li>
      <li>ferrier.tomas@correoluz.com</li>
      <li>Av. Ramón Quiroga 817 - 2do</li>
      <li>piso - Instituto Brandeck</li>
      <li>Córdoba, Argentina</li>
    </ul>
  </section>
</body>
</html>
```